Korimet Business Cards

Korimet is a software startup and we are looking for business cards that help convey our employee personalities, as well as the professionalism of the company.
Our company font is Comfortaa - and the company logo is attached (we are okay having the text beside the logo if applicable) where we can find the company colour scheme. Cards can be horizontal or vertical format.
We are looking for a two sided business card - on the front we will see the personal details of the employee (name, position, email and phone number), and then on the back, we will see the business details (name and logo, address, phone number, website, email, company tagline: "Accelerating technology disruption in the automotive market")
We want the design to be clean and simple, but also fun, modern, and capturing of a young startup vibe.

```html
<!DOCTYPE html>
<html lang="en">
<head>
<meta charset="utf-8">
<title>Korimet Business Cards</title>
<link rel="stylesheet" href="https://fonts.googleapis.com/css2?family=Comfortaa:wght@400;600;700&display=swap">
<style>
  :root {
    --backdrop: #d8d8da;
    --card: #1b1b1d;
    --ink: #f2f2f4;
    --ink-soft: #cfcfd4;
    --violet: #4a3ad4;
    --orchid: #a23cc2;
    --magenta: #c43aa6;
    --plum: #6a4bd8;
  }
  * { box-sizing: border-box; margin: 0; padding: 0; }
  html, body {
    width: 1200px; height: 800px; overflow: hidden;
    background: var(--backdrop);
    font-family: "Comfortaa", sans-serif;
  }
  .canvas {
    position: relative; width: 1200px; height: 800px;
    display: flex; align-items: center; justify-content: center; gap: 40px;
  }
  .card {
    position: relative;
    width: 540px; height: 310px;
    background: var(--card);
    border-radius: 20px;
    overflow: hidden;
  }
  /* Front: personal details */
  .brand-mark {
    position: absolute; top: 40px; right: 40px;
    display: flex; align-items: center; gap: 14px;
  }
  .brand-dot {
    width: 70px; height: 70px; border-radius: 50%;
    background: linear-gradient(135deg, var(--violet), var(--magenta));
  }
  .brand-name {
    font-weight: 700; font-size: 40px; color: var(--ink);
    letter-spacing: 0.5px;
  }
  .person {
    position: absolute; left: 36px; bottom: 32px;
    color: var(--ink);
  }
  .person-name {
    font-weight: 700; font-size: 20px; letter-spacing: 1px;
    color: var(--violet);
  }
  .person-role {
    font-size: 13px; color: var(--orchid); margin-top: 3px;
  }
  .address {
    font-size: 12px; line-height: 1.45; margin-top: 12px; color: var(--ink-soft);
  }
  .contact-list { list-style: none; margin-top: 12px; }
  .contact-list li {
    display: flex; align-items: center; gap: 8px;
    font-size: 12px; line-height: 1.5; color: var(--ink-soft);
  }
  .contact-list svg { width: 11px; height: 11px; flex: none; }
  .contact-list svg * { fill: none; stroke: var(--magenta); stroke-width: 2; stroke-linecap: round; stroke-linejoin: round; }

  /* Back: company side */
  .company-mark {
    position: absolute; left: 50%; top: 42%;
    transform: translate(-50%, -50%);
    display: flex; align-items: center; gap: 18px;
  }
  .company-dot {
    width: 62px; height: 62px; border-radius: 50%;
    background: linear-gradient(135deg, var(--violet), var(--magenta));
  }
  .company-name {
    font-weight: 600; font-size: 58px; color: var(--ink);
  }
  .tagline {
    position: absolute; left: 0; right: 0; bottom: 40px;
    text-align: center; font-size: 13.5px; color: var(--ink-soft);
    letter-spacing: 0.3px;
  }
</style>
</head>
<body>
<main class="canvas">
  <section class="card card-front" aria-label="Front of card">
    <div class="brand-mark">
      <span class="brand-dot"></span>
      <span class="brand-name">korimet</span>
    </div>
    <div class="person">
      <h1 class="person-name">DANIEL ROWE</h1>
      <p class="person-role">President</p>
      <p class="address">1420 Juniper Court<br>Fairbanks, Alaska 99701</p>
      <ul class="contact-list">
        <li><svg viewBox="0 0 12 12"><path d="M2 1.5l2 0 1 2.5-1.3 1a6 6 0 0 0 3.3 3.3l1-1.3 2.5 1v2a1 1 0 0 1-1 1A9 9 0 0 1 1 2.5a1 1 0 0 1 1-1z"/></svg>555-204-7731</li>
        <li><svg viewBox="0 0 12 12"><rect x="3" y="1" width="6" height="10" rx="1"/><path d="M5.5 9h1"/></svg>555-318-6624</li>
        <li><svg viewBox="0 0 12 12"><rect x="1" y="4" width="10" height="5" rx="1"/><path d="M3 4V1h6v3M3 9v2h6V9"/></svg>555-472-1190</li>
        <li><svg viewBox="0 0 12 12"><rect x="1" y="2.5" width="10" height="7" rx="1"/><path d="M1 3l5 4 5-4"/></svg>info@korimet.com</li>
        <li><svg viewBox="0 0 12 12"><circle cx="6" cy="6" r="5"/><path d="M1 6h10M6 1c2 2 2 8 0 10M6 1c-2 2-2 8 0 10"/></svg>www.korimet.com</li>
      </ul>
    </div>
  </section>

  <section class="card card-back" aria-label="Back of card">
    <div class="company-mark">
      <span class="company-dot"></span>
      <span class="company-name">korimet</span>
    </div>
    <p class="tagline">Accelerating technology disruption in the automotive market</p>
  </section>
</main>
</body>
</html>
```